Cyber security firm needs to have a new look and modren website design

Valtrix Corp is already established and looking to improve the feel and UI of the site and cause potential clients to say "wow, let's contact them".
We provide cybersecurity assessment consulting services helping our clients to feel safer than they are now with a straightforward approach to data safety, as the current frameworks and regulations are NOT affective anymore.

the current site is: www.valtrix-demo.biz

Please check the following sites:
quorvane.example
brindle-guard.example
https://www.halvenmoor.example

HomePage Design:
In general: we want to tell the viewer that it's a digital war out there, which is not a simple one. If not taking care of it will have causalities: https://www.halvenmoor.example/ see picture? See that and some what I'm afraid.... I need some assurance and safety...
1. Do not use the existing site content / design.
2. Do not use the 3 simple steps
3. Have slides top as it is now:
A Hacker Is Knocking, Are You READY? (and a matching picture)
4. Contact form on the right
5. 4 block services:
Web Application Security.
Internal / External Vulnerability Assessments.
Penetration Testing.
Malware Attack Simulation.
6. Recent News: 3 Blocks
7. Recent Posts: 3 Blocks
8. Under the contact form: Download out FREE Report Cybersecurity Assessment Framework
9. Top contact form search line.
10. Bottom page should show all links from top menu
11. This design should work on WordPress

Thanks.

Target Market(s)

Right now: Financials.
Looking to have to add more, will decide later.

Industry/Entity Type

Security

Coding

Coded - Design and coding required

Number of Pages Required

5+ page

Font styles to use
Other font styles liked:
• Caliberi

Requirements
Must have
• Our site is based on CMS: WordPress
• Should be progressive: to be showed on any device: PC, tablets and phones.
• Browsers: IE, Chrome and Firefox.
• Look serious, experts in their field and getting tasks done!
• Use the same fonts from:
• quorvane.example
• brindle-guard.example
• https://www.halvenmoor.example

```html
<!DOCTYPE html>
<html lang="en">
<head>
<meta charset="utf-8">
<title>Valtrix Corp – Cyber Security</title>
<link href="https://fonts.googleapis.com/css2?family=Open+Sans:wght@400;600;700&display=swap" rel="stylesheet">
<style>
:root{
  --red:#d7262e;
  --navy:#16314f;
  --navy-dark:#0f2238;
  --ink:#2a2a2a;
  --muted:#777;
  --line:#e2e2e2;
  --bg:#ffffff;
  --soft:#f4f5f7;
}
*{box-sizing:border-box;margin:0;padding:0}
html,body{width:690px;height:1200px;overflow:hidden;background:var(--bg)}
body{font-family:"Open Sans",Arial,sans-serif;color:var(--ink);font-size:7px;line-height:1.45}
.page{width:690px;height:1200px;position:relative;overflow:hidden}

/* header */
.site-header{height:50px;display:flex;align-items:center;justify-content:space-between;padding:0 45px;background:#fff;border-bottom:1px solid var(--line)}
.brand{display:flex;align-items:center;gap:6px}
.brand-mark{width:14px;height:14px;background:var(--red);border-radius:50%}
.brand-name{font-size:20px;font-weight:700;color:var(--navy);letter-spacing:.5px}
.brand-tag{font-size:6px;color:var(--muted);margin-left:2px;margin-top:10px}
.main-nav{display:flex;gap:2px}
.main-nav a{font-size:7px;color:var(--ink);text-decoration:none;padding:6px 9px;border-radius:2px}
.main-nav a.active{background:var(--red);color:#fff}

/* hero */
.hero{position:relative;height:285px;background:radial-gradient(circle at 50% 40%,#4a5f79 0%,#273646 45%,#121a24 100%)}
.hero-visual{position:absolute;inset:0}
.hero-arrow{position:absolute;top:128px;width:22px;height:22px;border-radius:50%;background:#fff;display:flex;align-items:center;justify-content:center}
.hero-arrow.prev{left:45px}
.hero-arrow.next{right:45px}

/* intro */
.intro{display:flex;gap:30px;padding:22px 45px 0;height:150px}
.intro-text{flex:1}
.intro h1{font-size:14px;font-weight:700;color:var(--ink);margin-bottom:8px}
.intro p{color:var(--muted);font-size:6.5px}
.btn{display:inline-block;background:var(--red);color:#fff;font-size:6.5px;font-weight:600;padding:5px 10px;border-radius:2px;margin-top:14px}
.intro-image{width:210px;height:105px;background:linear-gradient(135deg,#0a3f8f,#2b7fd6 55%,#d9b23a)}

/* services */
.services{padding:20px 45px 0;text-align:center;height:245px;border-top:1px solid var(--line)}
.section-title{font-size:12px;font-weight:700;color:var(--red);margin-bottom:4px}
.section-lede{color:var(--muted);font-size:6px;width:430px;margin:0 auto}
.service-grid{display:flex;justify-content:space-between;margin-top:22px}
.service{width:140px}
.service-icon{width:58px;height:58px;border-radius:50%;margin:0 auto 10px;background:#f1f2f4;display:flex;align-items:center;justify-content:center}
.service-icon.featured{background:var(--navy)}
.service h3{font-size:7px;font-weight:700;color:var(--ink);margin-bottom:4px}
.service p{font-size:6px;color:var(--muted)}

/* news & posts */
.updates{display:flex;gap:30px;padding:18px 45px 0;height:290px;background:var(--soft)}
.update-col{flex:1}
.update-col h2{font-size:11px;font-weight:700;color:var(--red);padding-bottom:5px;border-bottom:2px solid var(--red);display:inline-block;margin-bottom:10px}
.item{display:flex;gap:8px;padding-bottom:9px;margin-bottom:9px;border-bottom:1px solid var(--line)}
.thumb{width:78px;height:54px;flex:none}
.t1{background:linear-gradient(135deg,#0c1f4a,#2d59b8)}
.t2{background:linear-gradient(135deg,#07102a,#2a6fd0)}
.t3{background:linear-gradient(135deg,#152043,#3f78c9)}
.t4{background:linear-gradient(135deg,#1d1d2a,#7c8aa3)}
.t5{background:linear-gradient(135deg,#394350,#b5bfc9)}
.t6{background:linear-gradient(135deg,#7a0c10,#d7262e)}
.item h4{font-size:7px;color:var(--red);font-weight:700}
.item .date{font-size:5.5px;color:var(--muted)}
.item p{font-size:6px;color:var(--muted)}
.item .more{font-size:6px;color:var(--red);font-weight:600}

/* footer */
.site-footer{background:var(--navy);color:#cdd6e2;height:155px;padding:18px 45px 0;display:flex;gap:28px}
.site-footer h5{font-size:9px;color:#fff;font-weight:700;margin-bottom:10px}
.f-contact{width:150px}
.f-contact li{list-style:none;display:flex;gap:5px;align-items:flex-start;font-size:6px;margin-bottom:5px}
.f-logo{display:flex;align-items:center;gap:5px;margin-top:6px}
.f-logo span{font-size:14px;font-weight:700;color:#fff}
.f-logo i{width:10px;height:10px;background:var(--red);border-radius:50%}
.f-form{flex:1}
.form-grid{display:flex;gap:8px}
.form-fields{flex:1;display:flex;flex-direction:column;gap:5px}
.field{height:14px;background:#fff;border-radius:1px;font-size:5.5px;color:#999;padding:3px 4px}
.form-msg{flex:1;display:flex;flex-direction:column;gap:5px}
.form-msg .field{height:33px}
.send{background:#fff;color:var(--navy);font-size:6px;padding:3px 8px;width:28px;border-radius:1px}
.f-social{width:120px}
.f-social li{list-style:none;display:flex;align-items:center;gap:6px;font-size:7px;color:#fff;margin-bottom:7px}
.f-social i{width:13px;height:13px;border-radius:50%;background:#fff;display:block}
.bottom-bar{height:25px;background:var(--navy-dark);display:flex;align-items:center;justify-content:space-between;padding:0 45px;color:#8b97a8;font-size:5.5px}
.bottom-bar nav{display:flex;gap:12px}
</style>
</head>
<body>
<div class="page">
  <header class="site-header">
    <div class="brand">
      <span class="brand-mark"></span>
      <span class="brand-name">VALTRIX</span>
      <span class="brand-tag">safeguarding your data</span>
    </div>
    <nav class="main-nav">
      <a class="active">Home</a><a>About</a><a>Service</a><a>Partners</a><a>Event</a><a>Media</a><a>Contact us</a>
    </nav>
  </header>

  <section class="hero">
    <div class="hero-visual" role="img" aria-label="Security specialists in a dark room working with glowing panels labelled confidentiality, availability and integrity"></div>
    <span class="hero-arrow prev"><svg width="8" height="8" viewBox="0 0 8 8"><path d="M5.5 1L2.5 4l3 3" fill="none" stroke="#333" stroke-width="1.4"/></svg></span>
    <span class="hero-arrow next"><svg width="8" height="8" viewBox="0 0 8 8"><path d="M2.5 1l3 3-3 3" fill="none" stroke="#333" stroke-width="1.4"/></svg></span>
  </section>

  <section class="intro">
    <div class="intro-text">
      <h1>Hacker is Knocking, Are you READY?</h1>
      <p>Lorem Ipsum is simply dummy text of the printing and typesetting industry. Lorem Ipsum has been the industry's standard dummy text ever since the 1500s, when an unknown printer took a galley of type and scrambled it to make a type specimen book. It has survived not only five centuries, but also the leap into electronic typesetting.</p>
      <span class="btn">Read More</span>
    </div>
    <div class="intro-image" role="img" aria-label="Golden padlock resting on a blue circuit board"></div>
  </section>

  <section class="services">
    <h2 class="section-title">Lorem ipsum dolor sit amet</h2>
    <p class="section-lede">Lorem ipsum dolor sit amet, consectetur adipiscing elit, sed do eiusmod tempor incididunt ut labore et dolore magna aliqua. Ut enim ad minim veniam, quis nostrud exercitation ullamco laboris.</p>
    <div class="service-grid">
      <div class="service">
        <div class="service-icon featured"><svg width="22" height="22" viewBox="0 0 24 24"><path d="M12 2l8 3v6c0 5-3.5 9-8 11-4.5-2-8-6-8-11V5z" fill="#fff"/><path d="M8.5 12l2.5 2.5 4.5-5" fill="none" stroke="#16314f" stroke-width="2"/></svg></div>
        <h3>Web Application Security</h3>
        <p>Lorem Ipsum is simply dummy text of the printing and typesetting industry. Lorem Ipsum has been the industry's standard.</p>
      </div>
      <div class="service">
        <div class="service-icon"><svg width="22" height="22" viewBox="0 0 24 24" fill="none" stroke="#16314f" stroke-width="1.8"><circle cx="7" cy="7" r="3"/><circle cx="17" cy="17" r="3"/><path d="M10 7h7v7M14 17H7v-7"/></svg></div>
        <h3>Internal / External Vulnerability Assessments</h3>
        <p>Lorem Ipsum is simply dummy text of the printing and typesetting industry. Lorem Ipsum</p>
      </div>
      <div class="service">
        <div class="service-icon"><svg width="22" height="22" viewBox="0 0 24 24"><rect x="5" y="10" width="14" height="11" rx="1.5" fill="#16314f"/><path d="M8 10V7a4 4 0 018 0v3" fill="none" stroke="#16314f" stroke-width="2"/></svg></div>
        <h3>Penetration Testing</h3>
        <p>Lorem Ipsum is simply dummy text of the printing and typesetting industry. Lorem Ipsum has been the industry's standard.</p>
      </div>
      <div class="service">
        <div class="service-icon"><svg width="22" height="22" viewBox="0 0 24 24" fill="none" stroke="#16314f" stroke-width="1.8"><rect x="3" y="4" width="18" height="12" rx="1"/><path d="M8 20h8M12 16v4"/><path d="M12 7v4M12 13v.5"/></svg></div>
        <h3>Malware Attack Simulation</h3>
        <p>Lorem Ipsum is simply dummy text of the printing and typesetting industry. Lorem Ipsum has been the industry's standard.</p>
      </div>
    </div>
  </section>

  <section class="updates">
    <div class="update-col">
      <h2>Recent News</h2>
      <article class="item"><div class="thumb t1" role="img" aria-label="Blue digital network graphic"></div><div><h4>Lorem Ipsum</h4><p>Lorem Ipsum is simply dummy text of the printing and typesetting industry. Lorem Ipsum has been the industry's standard dummy text ever.</p><span class="more">Read more</span></div></article>
      <article class="item"><div class="thumb t2" role="img" aria-label="Glowing blue data stream"></div><div><h4>Lorem Ipsum</h4><p>Lorem Ipsum is simply dummy text of the printing and typesetting industry. Lorem Ipsum has been the industry's standard dummy text ever.</p><span class="more">Read more</span></div></article>
      <article class="item"><div class="thumb t3" role="img" aria-label="Digital lock on blue background"></div><div><h4>Lorem Ipsum</h4><p>Lorem Ipsum is simply dummy text of the printing and typesetting industry. Lorem Ipsum has been the industry's standard dummy text ever.</p><span class="more">Read more</span></div></article>
    </div>
    <div class="update-col">
      <h2>Recent Posts</h2>
      <article class="item"><div class="thumb t4" role="img" aria-label="Hands typing on a keyboard"></div><div><h4>Lorem Ipsum</h4><span class="date">25.06.2015</span><p>Lorem Ipsum is simply dummy text of the printing and typesetting industry. Lorem Ipsum has been the industry's standard.</p><span class="more">Read more</span></div></article>
      <article class="item"><div class="thumb t5" role="img" aria-label="Laptop keyboard close-up"></div><div><h4>Lorem Ipsum</h4><span class="date">25.06.2015</span><p>Lorem Ipsum is simply dummy text of the printing and typesetting industry. Lorem Ipsum has been the industry's standard.</p><span class="more">Read more</span></div></article>
      <article class="item"><div class="thumb t6" role="img" aria-label="Red stop key on a keyboard"></div><div><h4>Lorem Ipsum</h4><span class="date">25.06.2015</span><p>Lorem Ipsum is simply dummy text of the printing and typesetting industry. Lorem Ipsum has been the industry's standard.</p><span class="more">Read more</span></div></article>
    </div>
  </section>

  <footer class="site-footer">
    <div class="f-contact">
      <h5>Contact Info</h5>
      <ul>
        <li><svg width="7" height="8" viewBox="0 0 10 12"><path d="M5 0a4 4 0 00-4 4c0 3 4 8 4 8s4-5 4-8a4 4 0 00-4-4z" fill="#fff"/></svg><span>42 Harbor Lane 3rd Floor<br>Newport, ST 00000</span></li>
        <li><svg width="7" height="7" viewBox="0 0 10 10"><path d="M2 0l2 2-1 2 3 3 2-1 2 2-2 2C4 10 0 6 0 2z" fill="#fff"/></svg><span>1-800-555-0142</span></li>
        <li><svg width="7" height="6" viewBox="0 0 10 8"><rect width="10" height="8" fill="#fff"/><path d="M0 0l5 4 5-4" fill="none" stroke="#16314f"/></svg><span>info@valtrix-demo.biz</span></li>
      </ul>
      <div class="f-logo"><i></i><span>VALTRIX</span></div>
    </div>
    <div class="f-form">
      <h5>Contact form</h5>
      <div class="form-grid">
        <div class="form-fields"><div class="field">Name</div><div class="field">Email</div><div class="field">Phone</div></div>
        <div class="form-msg"><div class="field">Message</div><div class="send">Send</div></div>
      </div>
    </div>
    <div class="f-social">
      <h5>Social Media</h5>
      <ul>
        <li><i></i>Friendlink</li>
        <li><i></i>Chirper</li>
        <li><i></i>Searchly</li>
      </ul>
    </div>
  </footer>
  <div class="bottom-bar">
    <span>© All rights reserved Valtrix Corp 2000-2015</span>
    <nav><span>Home</span><span>About</span><span>Service</span><span>Partners</span><span>Event</span><span>Media</span><span>Contact us</span></nav>
  </div>
</div>
</body>
</html>
```